I need a Label design for my copper 71 kombucha brand that is launching soon

I want a label to go on my copper 71 kombucha bottle.
I have a logo image uploaded in the files but I am open to changes to this logo or even a completely New one if you think you can do better. This logo is based on the idea of an s-shaped naga. I particularly like the nagas from temples in luang prabang.
I also want to include the slogan - dare to be delicious.
The label should be some kind of oval at 80mm high by 70mm wide.
The label will go on a clear glass bottle. The kombucha will be visible and comes in different shades of red,yellow and purple.
The word kombucha should be clearly visible.
i want a very colorful, playful label. I'm very keen to see your ideas and I want something original.
Fermented foods and beverages

```html
<!DOCTYPE html>
<html lang="en">
<head>
<meta charset="utf-8">
<title>copper 71 Kombucha — Label Range</title>
<link rel="stylesheet" href="https://fonts.googleapis.com/css2?family=Montserrat:wght@500;600&family=Barlow+Semi+Condensed:wght@500&family=Barlow:wght@700&family=Kaushan+Script&display=swap">
<style>
  :root {
    --page: #ffffff;
    --ink: #ffffff;
    --plum: #8a4389;
    --tangerine: #e57412;
    --cherry: #df2d39;
  }
  html, body {
    margin: 0;
    padding: 0;
    overflow: hidden;
    background: var(--page);
  }
  .sheet {
    position: relative;
    width: 1102px;
    height: 1200px;
    overflow: hidden;
    background: var(--page);
  }
  .label {
    position: absolute;
    width: 440px;
    height: 500px;
  }
  .label--plum      { left: 74px;  top: 73px;  --label-bg: var(--plum); }
  .label--tangerine { left: 591px; top: 85px;  --label-bg: var(--tangerine); }
  .label--cherry    { left: 320px; top: 554px; --label-bg: var(--cherry); }

  .label__body { fill: var(--label-bg); }
  .label__mark { fill: none; stroke: var(--ink); stroke-width: 5; }
  .label__brand {
    font-family: "Montserrat", sans-serif;
    font-weight: 500;
    fill: var(--ink);
    text-anchor: middle;
  }
  .label__brand--name { font-size: 44px; letter-spacing: -1px; }
  .label__brand--number { font-size: 31px; font-weight: 600; }
  .label__product {
    font-family: "Kaushan Script", cursive;
    font-size: 100px;
    fill: var(--ink);
  }
  .label__volume {
    font-family: "Barlow Semi Condensed", sans-serif;
    font-weight: 500;
    font-size: 18px;
    fill: var(--ink);
  }
  .label__volume--metric { text-anchor: end; }
  .label__slogan {
    font-family: "Barlow", sans-serif;
    font-weight: 700;
    font-size: 14px;
    letter-spacing: 9px;
    fill: var(--ink);
  }
</style>
</head>
<body>
<main class="sheet">

  <svg class="label label--plum" viewBox="0 0 440 500" aria-label="copper 71 Kombucha label, plum">
    <defs>
      <path id="slogan-arc-plum" d="M 70 372 Q 220 522 372 372"/>
    </defs>
    <ellipse class="label__body" cx="220" cy="250" rx="215" ry="246"/>
    <circle class="label__mark" cx="220" cy="83" r="31"/>
    <text class="label__brand label__brand--name" x="220" y="166">copper</text>
    <text class="label__brand label__brand--number" x="220" y="200">71</text>
    <text class="label__product" x="48" y="308" textLength="346" lengthAdjust="spacingAndGlyphs">Kombucha</text>
    <text class="label__volume" x="44" y="351">4 FL OZ</text>
    <text class="label__volume label__volume--metric" x="393" y="351">120ML</text>
    <text class="label__slogan"><textPath href="#slogan-arc-plum" startOffset="50%" text-anchor="middle">DARE TO BE DELICIOUS</textPath></text>
  </svg>

  <svg class="label label--tangerine" viewBox="0 0 440 500" aria-label="copper 71 Kombucha label, tangerine">
    <defs>
      <path id="slogan-arc-tangerine" d="M 70 372 Q 220 522 372 372"/>
    </defs>
    <ellipse class="label__body" cx="220" cy="250" rx="215" ry="246"/>
    <circle class="label__mark" cx="220" cy="83" r="31"/>
    <text class="label__brand label__brand--name" x="220" y="166">copper</text>
    <text class="label__brand label__brand--number" x="220" y="200">71</text>
    <text class="label__product" x="48" y="308" textLength="346" lengthAdjust="spacingAndGlyphs">Kombucha</text>
    <text class="label__volume" x="44" y="351">4 FL OZ</text>
    <text class="label__volume label__volume--metric" x="393" y="351">120ML</text>
    <text class="label__slogan"><textPath href="#slogan-arc-tangerine" startOffset="50%" text-anchor="middle">DARE TO BE DELICIOUS</textPath></text>
  </svg>

  <svg class="label label--cherry" viewBox="0 0 440 500" aria-label="copper 71 Kombucha label, cherry">
    <defs>
      <path id="slogan-arc-cherry" d="M 70 372 Q 220 522 372 372"/>
    </defs>
    <ellipse class="label__body" cx="220" cy="250" rx="215" ry="246"/>
    <circle class="label__mark" cx="220" cy="83" r="31"/>
    <text class="label__brand label__brand--name" x="220" y="166">copper</text>
    <text class="label__brand label__brand--number" x="220" y="200">71</text>
    <text class="label__product" x="48" y="308" textLength="346" lengthAdjust="spacingAndGlyphs">Kombucha</text>
    <text class="label__volume" x="44" y="351">4 FL OZ</text>
    <text class="label__volume label__volume--metric" x="393" y="351">120ML</text>
    <text class="label__slogan"><textPath href="#slogan-arc-cherry" startOffset="50%" text-anchor="middle">DARE TO BE DELICIOUS</textPath></text>
  </svg>

</main>
</body>
</html>
```